Trevolant Consulting Card Design

Create a card design for the company.

Target Market(s)

B2B

Industry/Entity Type

Management Consulting

Contact Information for Business Card

Name; Role; email; phone; website;

Colors
0555a3
3276b5
85abd2
cee9f5

```html
<!DOCTYPE html>
<html lang="en">
<head>
<meta charset="utf-8">
<title>Trevolant Consulting — Business Card</title>
<link rel="stylesheet" href="https://fonts.googleapis.com/css2?family=Ubuntu:wght@300;400;700&display=swap">
<style>
  :root {
    --brand-deep: #0555a3;
    --brand-mid: #3276b5;
    --brand-soft: #85abd2;
    --brand-pale: #cee9f5;
    --ink-grey: #6d6f73;
    --edge-grey: #5c5e62;
    --card-white: #fbfbfb;
    --page-bg: #ecedef;
  }
  * { margin: 0; padding: 0; box-sizing: border-box; }
  html, body {
    width: 1200px; height: 1022px; overflow: hidden;
    background: var(--page-bg);
    font-family: "Ubuntu", Arial, sans-serif;
  }
  .business-card {
    position: absolute; left: 150px; top: 254px;
    width: 900px; height: 514px;
    background: linear-gradient(160deg, #ffffff 0%, var(--card-white) 60%, #f1f2f3 100%);
    box-shadow: 0 10px 30px rgba(0,0,0,0.12);
    overflow: hidden;
  }
  .edge-tab-grey {
    position: absolute; left: 0; top: 312px; width: 9px; height: 54px;
    background: var(--edge-grey);
  }
  .edge-tab-blue {
    position: absolute; left: 0; top: 378px; width: 9px; height: 44px;
    background: var(--brand-mid);
  }
  .brand-block { position: absolute; left: 58px; top: 262px; }
  .wordmark {
    font-weight: 700; font-size: 66px; line-height: 1;
    color: var(--brand-deep); letter-spacing: -1px;
  }
  .tagline {
    margin-top: 4px; font-weight: 300; font-size: 19px;
    letter-spacing: 1.2px; color: var(--ink-grey); text-transform: uppercase;
    white-space: nowrap;
  }
  .person { position: absolute; left: 100px; top: 372px; }
  .person-name { font-size: 27px; color: var(--brand-mid); font-weight: 400; }
  .person-role { font-size: 16px; color: var(--ink-grey); font-weight: 300; margin-top: 2px; margin-left: 30px; }
  .contact-list {
    position: absolute; left: 490px; top: 300px;
    list-style: none; font-size: 18px; font-weight: 300; color: var(--ink-grey);
  }
  .contact-list li { display: flex; align-items: center; gap: 12px; height: 40px; }
  .contact-list svg { width: 16px; height: 16px; flex: none; }
  .brand-emblem-area {
    position: absolute; left: 470px; top: 10px; width: 420px; height: 270px;
  }
</style>
</head>
<body>
  <main class="business-card">
    <svg class="brand-emblem-area" viewBox="0 0 420 270" role="img" aria-label="Trevolant brand emblem area">
      <defs>
        <linearGradient id="emblem-tone" x1="0" y1="0" x2="1" y2="0">
          <stop offset="0" stop-color="var(--brand-pale)"/>
          <stop offset="1" stop-color="#e3e4e6"/>
        </linearGradient>
      </defs>
      <circle cx="210" cy="135" r="125" fill="url(#emblem-tone)"/>
    </svg>

    <div class="edge-tab-grey"></div>
    <div class="edge-tab-blue"></div>

    <div class="brand-block">
      <div class="wordmark">Trevolant</div>
      <div class="tagline">Strengthening your teams</div>
    </div>

    <div class="person">
      <div class="person-name">Ana Moreto</div>
      <div class="person-role">Partner</div>
    </div>

    <ul class="contact-list">
      <li>
        <svg viewBox="0 0 16 16" aria-hidden="true"><path d="M4 1.5l2.5 3-1.5 1.8c.8 1.8 2.2 3.2 4 4l1.8-1.5 3 2.5-1.6 2.2C8 13 3 8 2 3.1z" fill="var(--brand-mid)"/></svg>
        <span>+351 900 482 173</span>
      </li>
      <li>
        <svg viewBox="0 0 16 16" aria-hidden="true"><rect x="1.5" y="3.5" width="13" height="9" fill="none" stroke="var(--brand-mid)" stroke-width="1.5"/><path d="M1.5 3.5L8 9l6.5-5.5" fill="none" stroke="var(--brand-mid)" stroke-width="1.5"/></svg>
        <span>ana.moreto@trevolant.com</span>
      </li>
      <li>
        <svg viewBox="0 0 16 16" aria-hidden="true"><circle cx="8" cy="8" r="6.5" fill="none" stroke="var(--brand-mid)" stroke-width="1.4"/><ellipse cx="8" cy="8" rx="2.8" ry="6.5" fill="none" stroke="var(--brand-mid)" stroke-width="1.2"/><path d="M1.5 8h13M2.5 4.8h11M2.5 11.2h11" stroke="var(--brand-mid)" stroke-width="1.1"/></svg>
        <span>www.trevolant.com</span>
      </li>
    </ul>
  </main>
</body>
</html>
```